Create a business Card for a Women Owned Business Body Positive Company. The winner we hope to work with on other projects coming up for grand opening for flyers, postcards, email marketing, facebook page, stationary, labels, tshirt design....
We would like if possible in the background of the card a infinity symbol or crown if it fits into the design if not it's ok. But I am open to all suggestions we had alot problems with the our new logo being created this time sad to say :(

Our colors are Royal Purple, Grey, Black Thank you in advance for your talent, you hard work and your submissions!
Delia and Nadine :)
Updates

my Logo is velvet harbor boutique which is purple and has a heart and infinity sign in it and my colors are purple silver and black only of another card i had done nothing else. My logo is VELVET HARBOR BOUTIQUE LOGO

Industry/Entity Type

Retail

Contact Information for Business Card

website: www.velvtharborboutiques.example email: sales@velvetharborboutique.example
Delia Pruett & Nadine Kolb Owners

Font styles to use
Script

Colors
b768aa

Requirements
Must have
• COLORS ARE PURPLE BLACK AND GREY
Nice to have
• INFINITY SIGNING IN THE BACKGROUND

```html
<!DOCTYPE html>
<html lang="en">
<head>
<meta charset="utf-8">
<title>Velvet Harbor Boutique – Business Card</title>
<link rel="stylesheet" href="https://fonts.googleapis.com/css2?family=Cinzel:wght@400;600&display=swap">
<style>
  :root {
    --royal-purple: #6a3fa3;
    --deep-purple: #4a2482;
    --card-white: #f4f4f4;
    --ink: #1d1d1d;
    --stage: #e6e4e8;
    --on-purple: #ffffff;
  }
  * { box-sizing: border-box; margin: 0; padding: 0; }
  html, body {
    width: 1200px; height: 1000px; overflow: hidden;
    background: var(--stage);
    font-family: "Cinzel", "Times New Roman", serif;
  }
  .canvas { position: relative; width: 1200px; height: 1000px; }
  .card {
    position: absolute; left: 250px; width: 700px; height: 400px;
    border-radius: 26px;
    box-shadow: 0 10px 28px rgba(0,0,0,.18);
    overflow: hidden;
  }

  /* Front */
  .card-front { top: 60px; background: var(--royal-purple); color: var(--on-purple); }
  .front-rule { position: absolute; left: 150px; width: 400px; height: 2px; background: var(--on-purple); }
  .front-rule.top { top: 92px; }
  .front-rule.bottom { top: 252px; }
  .front-name {
    position: absolute; left: 0; right: 0; top: 120px;
    text-align: center; font-weight: 400; font-size: 50px; letter-spacing: 1px;
  }
  .front-sub {
    position: absolute; left: 0; right: 0; top: 198px;
    display: flex; justify-content: center; align-items: center; gap: 22px;
    font-size: 22px; line-height: 30px;
  }
  .front-sub .sub-word { letter-spacing: 9px; margin-right: -9px; }
  .front-sub .sub-rule { width: 90px; height: 2px; background: var(--on-purple); }
  .front-tagline {
    position: absolute; left: 110px; right: 110px; top: 290px;
    text-align: center; font-size: 19px; line-height: 1.35; letter-spacing: .5px;
  }

  /* Back */
  .card-back {
    top: 530px;
    background:
      repeating-linear-gradient(0deg, rgba(0,0,0,.018) 0 1px, transparent 1px 3px),
      repeating-linear-gradient(90deg, rgba(0,0,0,.018) 0 1px, transparent 1px 3px),
      var(--card-white);
    color: var(--ink);
  }
  .back-mark { position: absolute; left: 410px; top: 95px; width: 260px; color: var(--royal-purple); }
  .back-mark .mark-rule { height: 2px; background: var(--royal-purple); }
  .back-mark .mark-rule.dark { background: var(--ink); margin: 0 25px; }
  .back-mark .mark-name { font-size: 29px; text-align: center; margin: 6px 0 2px; }
  .back-mark .mark-sub { font-size: 13px; letter-spacing: 7px; text-indent: 7px; text-align: center; margin-bottom: 6px; color: var(--deep-purple); }

  .owners { position: absolute; left: 50px; top: 150px; padding-left: 34px; }
  .owners .marker { position: absolute; left: 0; top: 22px; }
  .owner-name { color: var(--deep-purple); font-size: 24px; line-height: 1.05; }
  .owner-role { font-size: 13px; letter-spacing: 1px; margin-top: 4px; }

  .contacts { position: absolute; left: 50px; top: 262px; list-style: none; }
  .contacts li { display: flex; align-items: center; gap: 10px; font-size: 15px; margin-bottom: 10px; }
  .contacts li:first-child { font-size: 19px; }
  .contacts svg { flex: none; }
</style>
</head>
<body>
<main class="canvas">

  <section class="card card-front" aria-label="Card front">
    <div class="front-rule top"></div>
    <h1 class="front-name">VELVET HARBOR</h1>
    <p class="front-sub"><span class="sub-rule"></span><span class="sub-word">BOUTIQUE</span><span class="sub-rule"></span></p>
    <div class="front-rule bottom"></div>
    <p class="front-tagline">Proudly providing unique clothing to all<br>women, young ladies &amp; princesses.</p>
  </section>

  <section class="card card-back" aria-label="Card back">
    <div class="back-mark">
      <div class="mark-rule"></div>
      <p class="mark-name">VELVET HARBOR</p>
      <p class="mark-sub">BOUTIQUE</p>
      <div class="mark-rule dark"></div>
    </div>

    <div class="owners">
      <svg class="marker" width="20" height="22" viewBox="0 0 20 22"><path d="M0 0 L20 11 L0 22 Z" fill="var(--deep-purple)"/></svg>
      <p class="owner-name">Delia Pruett</p>
      <p class="owner-name">Nadine Kolb</p>
      <p class="owner-role">OWNERS</p>
    </div>

    <ul class="contacts">
      <li>
        <svg width="18" height="18" viewBox="0 0 24 24"><circle cx="12" cy="12" r="12" fill="var(--royal-purple)"/><path d="M8 6.5c.6-.4 1.3-.3 1.6.3l1 2c.2.5.1 1-.3 1.3l-.8.6c.6 1.4 1.6 2.4 3 3l.6-.8c.3-.4.8-.5 1.3-.3l2 1c.6.3.7 1 .3 1.6-.9 1.3-2.4 1.6-3.8.9-2.5-1.2-4.4-3.1-5.6-5.6-.6-1.4-.3-2.9.7-4z" fill="#fff"/></svg>
        555-014-2288
      </li>
      <li>
        <svg width="18" height="18" viewBox="0 0 24 24"><circle cx="12" cy="12" r="12" fill="var(--royal-purple)"/><rect x="6" y="8" width="12" height="8.5" rx="1" fill="none" stroke="#fff" stroke-width="1.5"/><path d="M6.5 8.5 L12 13 L17.5 8.5" fill="none" stroke="#fff" stroke-width="1.5"/></svg>
        SALES@VELVETHARBORBOUTIQUE.EXAMPLE
      </li>
      <li>
        <svg width="18" height="18" viewBox="0 0 24 24"><circle cx="12" cy="12" r="12" fill="var(--royal-purple)"/><g fill="none" stroke="#fff" stroke-width="1.3"><circle cx="12" cy="12" r="6"/><ellipse cx="12" cy="12" rx="2.6" ry="6"/><path d="M6 12h12"/></g></svg>
        WWW.VELVTHARBORBOUTIQUES.EXAMPLE
      </li>
    </ul>
  </section>

</main>
</body>
</html>
```